Business card design needed

It's a new business in town.Something so the name stands out.I need a logo for the B.R.W
I may all so use the design as a sign on a building

Contact Information for Business Card

B.R.W
Brindlewood Auto Detailing
42 Fenwarra Crs
Brindlewood Vic 3799
Ph:(03)59284736
Mob:0417362958

```html
<!DOCTYPE html>
<html lang="en">
<head>
<meta charset="utf-8">
<title>Brindlewood Auto Detailing – Business Card</title>
<link rel="stylesheet" href="https://fonts.googleapis.com/css2?family=Oranienbaum&family=Open+Sans:wght@400&display=swap">
<style>
  :root {
    --brand-orange: #f26b22;
    --ink-black: #111111;
    --bar-black: #1a1a1a;
    --border-grey: #3a3a3a;
    --paper: #ffffff;
    --label-white: #ffffff;
  }
  html, body {
    margin: 0;
    padding: 0;
    overflow: hidden;
    background: var(--paper);
  }
  .business-card {
    display: block;
    width: 1200px;
    height: 692px;
    background: var(--paper);
  }
  .brand-tile { fill: var(--brand-orange); stroke: var(--border-grey); stroke-width: 9; }
  .brand-name {
    font-family: "Oranienbaum", "Times New Roman", serif;
    font-size: 96px;
    fill: var(--label-white);
  }
  .name-band { fill: var(--bar-black); stroke: var(--brand-orange); stroke-width: 9; }
  .business-name {
    font-family: "Oranienbaum", "Times New Roman", serif;
    font-size: 78px;
    fill: var(--label-white);
  }
  .address-line {
    font-family: "Oranienbaum", "Times New Roman", serif;
    fill: var(--ink-black);
  }
  .address-street { font-size: 74px; }
  .address-town { font-size: 90px; }
  .contact-strip { fill: var(--brand-orange); stroke: var(--border-grey); stroke-width: 9; }
  .contact-number {
    font-family: "Open Sans", Arial, sans-serif;
    font-size: 38px;
    fill: var(--label-white);
  }
</style>
</head>
<body>
<svg class="business-card" viewBox="0 0 1200 692" xmlns="http://www.w3.org/2000/svg" aria-labelledby="card-title">
  <title id="card-title">Brindlewood Auto Detailing business card</title>

  <g class="address-top">
    <text class="address-line address-street" x="503" y="208" textLength="348" lengthAdjust="spacingAndGlyphs">42 Fenwarra Crs</text>
  </g>

  <rect class="name-band" x="537" y="225" width="632" height="170" rx="62" ry="62"/>
  <text class="business-name" x="577" y="338" textLength="556" lengthAdjust="spacingAndGlyphs">Brindlewood Auto Detailing</text>

  <g class="brand-mark">
    <rect class="brand-tile" x="119" y="113" width="368" height="368" rx="46" ry="46" transform="rotate(45 303 297)"/>
    <text class="brand-name" x="303" y="330" text-anchor="middle">B.R.W</text>
  </g>

  <g class="address-bottom">
    <text class="address-line address-town" x="503" y="480" textLength="420" lengthAdjust="spacingAndGlyphs">Brindlewood Vic 3799</text>
  </g>

  <g class="contact-row">
    <rect class="contact-strip" x="67" y="589" width="1082" height="56" rx="28" ry="28"/>
    <text class="contact-number" x="82" y="631">Mob:0417362958</text>
    <text class="contact-number" x="1138" y="631" text-anchor="end">Ph:(03)59284736</text>
  </g>
</svg>
</body>
</html>
```